BarnLoft 2-page Flyer

Please use the attached content to design the flyer. Please note to use the previously designed logo and images from my website: www.barnloftco.example for the flyer. I prefer to only use the Owl for the logo and not the words

```html
<!DOCTYPE html>
<html lang="en">
<head>
<meta charset="utf-8">
<title>BarnLoft Two-Page Flyer</title>
<link href="https://fonts.googleapis.com/css2?family=Oswald:wght@500;600;700&family=Open+Sans:wght@400;600;700&display=swap" rel="stylesheet">
<style>
:root{
  --navy:#1c2a5c;
  --navy-deep:#131d44;
  --red:#e3262e;
  --green:#2fa84f;
  --ink:#2b2f3a;
  --paper:#ffffff;
  --stage:#d9d9d9;
  --muted:#5b6172;
}
*{box-sizing:border-box;margin:0;padding:0}
html,body{width:1200px;height:3000px;overflow:hidden}
body{background:var(--stage);font-family:"Open Sans",Arial,sans-serif;color:var(--ink);position:relative}
.page{position:absolute;left:60px;width:1080px;height:1420px;background:var(--paper);overflow:hidden;box-shadow:0 6px 24px rgba(0,0,0,.18)}
.page-front{top:60px}
.page-back{top:1520px}
.abs{position:absolute}
.heading{font-family:"Oswald",Impact,sans-serif;text-transform:uppercase;letter-spacing:.5px}

/* front */
.hero-globe{left:0;top:0;width:1080px;height:340px;background:linear-gradient(120deg,#0d1736 0%,#24407a 45%,#8aa3c9 70%,#1a2a55 100%)}
.title-bar{left:0;top:40px;width:760px;height:90px}
.title-text{left:40px;top:52px;font-size:48px;color:#fff;font-weight:600}
.title-text .accent{color:var(--red)}
.brand-mark{right:40px;top:30px;display:flex;align-items:center;gap:10px}
.brand-dot{width:56px;height:56px;border-radius:50%;background:var(--paper);border:4px solid var(--navy)}
.brand-name{font-family:"Oswald",Impact,sans-serif;font-weight:600;font-size:30px;color:#fff}
.portrait-frame{left:60px;top:250px;width:420px;height:380px;border:6px solid var(--red);background:var(--paper)}
.portrait{left:72px;top:262px;width:396px;height:356px;background:linear-gradient(180deg,#b7c2d6 0%,#6d5a52 60%,#2a2a30 100%)}
.intro-box{left:520px;top:360px;width:500px;padding:26px 30px;background:var(--red);color:#fff;font-size:22px;line-height:1.45;font-weight:600}
.services-title{left:60px;top:680px;font-size:54px;color:var(--green);font-weight:700}
.services{left:60px;top:780px;width:960px;display:grid;grid-template-columns:1fr 1fr;column-gap:60px;row-gap:34px}
.service{display:flex;align-items:center;gap:18px;font-size:22px;line-height:1.3;font-weight:600;color:var(--ink)}
.tick{flex:none;width:46px;height:46px}
.footer-front{left:0;top:1220px;width:1080px;height:200px}
.phone{left:50px;top:1282px;display:flex;align-items:center;gap:16px;color:#fff;font-family:"Oswald",Impact,sans-serif;font-size:46px;font-weight:600}
.contact-list{display:flex;flex-direction:column;gap:14px;color:#fff;font-size:22px;font-weight:600}
.contact-item{display:flex;align-items:center;gap:14px}
.contact-front{left:640px;top:1262px}
.icon{width:34px;height:34px;flex:none}

/* back */
.hero-ship{left:0;top:0;width:1080px;height:420px;background:linear-gradient(160deg,#cfe3f2 0%,#6fa6cf 35%,#b5563a 62%,#2d5c8a 100%)}
.cta-banner{left:0;top:330px;width:680px;height:150px}
.cta-text{left:40px;top:350px;font-size:46px;line-height:1.15;color:#fff;font-weight:700}
.label{background:var(--navy);color:#fff;font-size:30px;font-weight:600;padding:8px 26px}
.label-founder{left:40px;top:520px}
.founder-text{left:40px;top:590px;width:1000px;display:grid;grid-template-columns:1fr 1fr;column-gap:50px;font-size:19px;line-height:1.55;color:var(--muted)}
.label-why{left:40px;top:830px}
.reasons{left:40px;top:910px;width:580px;display:grid;grid-template-columns:1fr 1fr;column-gap:30px;row-gap:30px}
.reasons .service{font-size:19px}
.reasons .tick{width:40px;height:40px}
.founder-photo{left:640px;top:780px;width:440px;height:560px;background:linear-gradient(180deg,#e9edf2 0%,#c7ccd4 40%,#2a3550 100%)}
.contact-back{left:40px;top:1220px}
.contact-back .contact-list{color:var(--navy)}
.footer-back{left:0;top:1350px;width:1080px;height:70px}
</style>
</head>
<body>

<section class="page page-front" aria-label="Flyer page one">
  <div class="abs hero-globe" role="img" aria-label="Photo of a digital globe with glowing trade network lines"></div>
  <svg class="abs title-bar" viewBox="0 0 760 90" preserveAspectRatio="none"><polygon points="0,0 760,0 700,90 0,90" fill="var(--navy)"/></svg>
  <h1 class="abs heading title-text">Simplifying Global <span class="accent">Trade Compliance</span></h1>
  <div class="abs brand-mark"><span class="brand-dot"></span><span class="brand-name">BarnLoft</span></div>

  <div class="abs portrait-frame"></div>
  <div class="abs portrait" role="img" aria-label="Portrait photo of a smiling businesswoman"></div>
  <p class="abs intro-box">Helping small and mid-sized businesses confidently navigate U.S. import/export regulations.</p>

  <h2 class="abs heading services-title">Core Services</h2>
  <ul class="abs services" style="list-style:none">
    <li class="service"><svg class="tick" viewBox="0 0 46 46"><circle cx="23" cy="23" r="23" fill="var(--green)"/><path d="M13 24l7 7 13-15" fill="none" stroke="#fff" stroke-width="4" stroke-linecap="round" stroke-linejoin="round"/></svg>Import &amp; Export Compliance Advisory</li>
    <li class="service"><svg class="tick" viewBox="0 0 46 46"><circle cx="23" cy="23" r="23" fill="var(--green)"/><path d="M13 24l7 7 13-15" fill="none" stroke="#fff" stroke-width="4" stroke-linecap="round" stroke-linejoin="round"/></svg>Export Controls (EAR, ITAR, OFAC)</li>
    <li class="service"><svg class="tick" viewBox="0 0 46 46"><circle cx="23" cy="23" r="23" fill="var(--green)"/><path d="M13 24l7 7 13-15" fill="none" stroke="#fff" stroke-width="4" stroke-linecap="round" stroke-linejoin="round"/></svg>HTS Classification Guidance</li>
    <li class="service"><svg class="tick" viewBox="0 0 46 46"><circle cx="23" cy="23" r="23" fill="var(--green)"/><path d="M13 24l7 7 13-15" fill="none" stroke="#fff" stroke-width="4" stroke-linecap="round" stroke-linejoin="round"/></svg>PGA Compliance: FDA, USDA, EPA, FCC and others</li>
    <li class="service"><svg class="tick" viewBox="0 0 46 46"><circle cx="23" cy="23" r="23" fill="var(--green)"/><path d="M13 24l7 7 13-15" fill="none" stroke="#fff" stroke-width="4" stroke-linecap="round" stroke-linejoin="round"/></svg>Valuation &amp; Country of Origin Analysis</li>
    <li class="service"><svg class="tick" viewBox="0 0 46 46"><circle cx="23" cy="23" r="23" fill="var(--green)"/><path d="M13 24l7 7 13-15" fill="none" stroke="#fff" stroke-width="4" stroke-linecap="round" stroke-linejoin="round"/></svg>CBP Enforcement Support &amp; Penalty Mitigation</li>
    <li class="service"><svg class="tick" viewBox="0 0 46 46"><circle cx="23" cy="23" r="23" fill="var(--green)"/><path d="M13 24l7 7 13-15" fill="none" stroke="#fff" stroke-width="4" stroke-linecap="round" stroke-linejoin="round"/></svg>Trade Agreement Qualification (USMCA, GSP, etc.)</li>
    <li class="service"><svg class="tick" viewBox="0 0 46 46"><circle cx="23" cy="23" r="23" fill="var(--green)"/><path d="M13 24l7 7 13-15" fill="none" stroke="#fff" stroke-width="4" stroke-linecap="round" stroke-linejoin="round"/></svg>Internal Compliance Manuals &amp; Training</li>
  </ul>

  <svg class="abs footer-front" viewBox="0 0 1080 200" preserveAspectRatio="none">
    <rect x="0" y="0" width="1080" height="170" fill="var(--navy)"/>
    <polygon points="600,0 1080,0 1080,170 540,170" fill="var(--red)"/>
    <rect x="0" y="170" width="1080" height="30" fill="var(--red)"/>
  </svg>
  <div class="abs phone">
    <svg class="icon" viewBox="0 0 24 24" style="width:44px;height:44px"><path fill="#fff" d="M6.6 10.8a15.1 15.1 0 0 0 6.6 6.6l2.2-2.2a1 1 0 0 1 1-.25 11.4 11.4 0 0 0 3.6.57 1 1 0 0 1 1 1V20a1 1 0 0 1-1 1A17 17 0 0 1 3 4a1 1 0 0 1 1-1h3.5a1 1 0 0 1 1 1c0 1.25.2 2.45.57 3.57a1 1 0 0 1-.25 1z"/></svg>
    (555) 014-2290
  </div>
  <div class="abs contact-front contact-list">
    <span class="contact-item"><svg class="icon" viewBox="0 0 34 34"><circle cx="17" cy="17" r="15" fill="none" stroke="#fff" stroke-width="2.5"/><path d="M2 17h30M17 2c-6 8-6 22 0 30M17 2c6 8 6 22 0 30" fill="none" stroke="#fff" stroke-width="2"/></svg>www.barnloftco.example</span>
    <span class="contact-item"><svg class="icon" viewBox="0 0 34 34"><rect x="3" y="7" width="28" height="20" rx="2" fill="none" stroke="#fff" stroke-width="2.5"/><path d="M3 8l14 11 14-11" fill="none" stroke="#fff" stroke-width="2.5"/></svg>info@barnloftco.example</span>
  </div>
</section>

<section class="page page-back" aria-label="Flyer page two">
  <div class="abs hero-ship" role="img" aria-label="Photo of a container cargo ship at sea"></div>
  <svg class="abs cta-banner" viewBox="0 0 680 150" preserveAspectRatio="none"><polygon points="0,0 680,0 630,150 0,150" fill="var(--red)"/></svg>
  <h2 class="abs heading cta-text">Schedule Your Free<br>30-Minute Consultation</h2>

  <h3 class="abs heading label label-founder">Meet the Founder</h3>
  <div class="abs founder-text">
    <p>Dana Whitfield, founder and president of BarnLoftUSA LLC, brings over 20 years of experience in international trade and customs compliance. A licensed customs broker, Dana has guided importers and exporters through classification, valuation and regulatory reviews.</p>
    <p>Dana has helped companies of every size build practical compliance programs, resolve CBP inquiries and reduce penalty risk. Clients value clear advice, fast responses and a steady partner who understands how global trade really works.</p>
  </div>

  <h3 class="abs heading label label-why">Why Choose BarnLoftUSA?</h3>
  <ul class="abs reasons" style="list-style:none">
    <li class="service"><svg class="tick" viewBox="0 0 46 46"><circle cx="23" cy="23" r="23" fill="var(--green)"/><path d="M13 24l7 7 13-15" fill="none" stroke="#fff" stroke-width="4" stroke-linecap="round" stroke-linejoin="round"/></svg>Trusted by importers and exporters nationwide</li>
    <li class="service"><svg class="tick" viewBox="0 0 46 46"><circle cx="23" cy="23" r="23" fill="var(--green)"/><path d="M13 24l7 7 13-15" fill="none" stroke="#fff" stroke-width="4" stroke-linecap="round" stroke-linejoin="round"/></svg>Affordable, flexible service packages</li>
    <li class="service"><svg class="tick" viewBox="0 0 46 46"><circle cx="23" cy="23" r="23" fill="var(--green)"/><path d="M13 24l7 7 13-15" fill="none" stroke="#fff" stroke-width="4" stroke-linecap="round" stroke-linejoin="round"/></svg>Personalized service from a licensed broker</li>
    <li class="service"><svg class="tick" viewBox="0 0 46 46"><circle cx="23" cy="23" r="23" fill="var(--green)"/><path d="M13 24l7 7 13-15" fill="none" stroke="#fff" stroke-width="4" stroke-linecap="round" stroke-linejoin="round"/></svg>Deep knowledge of U.S. trade rules</li>
    <li class="service"><svg class="tick" viewBox="0 0 46 46"><circle cx="23" cy="23" r="23" fill="var(--green)"/><path d="M13 24l7 7 13-15" fill="none" stroke="#fff" stroke-width="4" stroke-linecap="round" stroke-linejoin="round"/></svg>Proven results in compliance audits</li>
    <li class="service"><svg class="tick" viewBox="0 0 46 46"><circle cx="23" cy="23" r="23" fill="var(--green)"/><path d="M13 24l7 7 13-15" fill="none" stroke="#fff" stroke-width="4" stroke-linecap="round" stroke-linejoin="round"/></svg>Quick turnaround on every request</li>
  </ul>

  <div class="abs founder-photo" role="img" aria-label="Photo of the founder in a suit, pointing toward the text"></div>

  <div class="abs contact-back contact-list">
    <span class="contact-item"><svg class="icon" viewBox="0 0 34 34"><circle cx="17" cy="17" r="17" fill="var(--red)"/><circle cx="17" cy="17" r="9" fill="none" stroke="#fff" stroke-width="2"/><path d="M8 17h18M17 8c-4 5-4 13 0 18M17 8c4 5 4 13 0 18" fill="none" stroke="#fff" stroke-width="1.6"/></svg>www.barnloftco.example</span>
    <span class="contact-item"><svg class="icon" viewBox="0 0 34 34"><circle cx="17" cy="17" r="17" fill="var(--red)"/><rect x="8" y="11" width="18" height="13" rx="1.5" fill="none" stroke="#fff" stroke-width="2"/><path d="M8 12l9 7 9-7" fill="none" stroke="#fff" stroke-width="2"/></svg>info@barnloftco.example</span>
  </div>

  <svg class="abs footer-back" viewBox="0 0 1080 70" preserveAspectRatio="none">
    <rect x="0" y="0" width="1080" height="70" fill="var(--navy)"/>
    <polygon points="0,0 260,0 220,70 0,70" fill="var(--red)"/>
  </svg>
</section>

</body>
</html>
```